Web Design for a Biotech Consulting Firm

We need a web site design for a new business based in Philadelphia called Corventa Dx. This is a consulting firm that will serve medical diagnostics industry, which is part of the life science/healthcare industry focusing on developing and marketing products that help in early detection, monitoring or management of diseases. Our consulting firm will help medical diagnostic companies to overcome key challenges in designing, evaluating and marketing new products.Our company name is Corventa Dx. Corventa is Latin word for "something" Dx represents diagnostics. The idea behind the name is that we help companies to transform the original, early product ideas ("nothing") into "something"; which is a product with full clinical utility that will help to improve health and well-being.The web site should use the visual feel of the logo (attached), be modern, simple and clean looking and represent creativity, innovation, scientific thinking and progress.
Updates

Wix Design is acceptable

Industry/Entity Type

Biotechnology

Coding

Coded - Design and coding required

Number of Pages Required

1 page

Font styles to use
Sans Serif

Requirements
Must have
• simple, clean look couple of pages
Should not have
• a lot of pages

```html
<!DOCTYPE html>
<html lang="en">
<head>
<meta charset="utf-8">
<title>Corventa Dx — Outside The Box Thinking</title>
<link href="https://fonts.googleapis.com/css2?family=Montserrat:wght@400;600;700&family=Roboto:wght@300;400;500&display=swap" rel="stylesheet">
<style>
:root{
  --blue:#1c6cf2;
  --blue-soft:#5f9cf6;
  --ink:#1b1b1b;
  --text:#333;
  --footer:#262528;
  --white:#fff;
}
*{margin:0;padding:0;box-sizing:border-box}
html,body{width:1200px;height:3449px;overflow:hidden;background:var(--white)}
body{position:relative;font-family:'Roboto',sans-serif;color:var(--text)}
.abs{position:absolute}
/* header */
.site-header{position:absolute;left:0;top:0;width:1200px;height:123px;background:var(--white)}
.brand{position:absolute;left:90px;top:32px;display:flex;align-items:center;gap:10px;font-family:'Montserrat',sans-serif;font-weight:600;font-size:26px;color:var(--blue)}
.brand-square{width:14px;height:14px;background:var(--blue)}
.nav{position:absolute;top:54px;font-size:15px;font-weight:500;color:var(--ink);letter-spacing:.2px}
.nav.active{color:var(--blue)}
.social-block{position:absolute;left:912px;top:0;width:288px;height:123px;background:var(--blue);display:flex;align-items:center;justify-content:center;gap:26px}
.dot{width:18px;height:18px;border-radius:50%;background:var(--white)}
/* hero */
.hero{position:absolute;left:0;top:123px;width:1200px;height:622px;background:linear-gradient(110deg,#c9dcf5 0%,#5d9cee 25%,#9cc3f2 50%,#dbe8f7 70%,#c3c6ea 85%,#e9eef8 100%)}
.hero-kicker{position:absolute;left:0;top:318px;width:1200px;text-align:center;font-weight:300;font-size:40px;color:var(--ink)}
.hero-title{position:absolute;left:0;top:370px;width:1200px;text-align:center;font-family:'Montserrat',sans-serif;font-weight:700;font-size:55px;color:var(--blue)}
.btn-frame{position:absolute;left:505px;top:485px;width:198px;height:50px;border:1px solid var(--blue)}
.btn-primary{position:absolute;left:498px;top:478px;width:198px;height:50px;background:var(--blue);color:var(--white);font-size:17px;font-weight:500;display:flex;align-items:center;justify-content:center}
.slider-dots{position:absolute;left:550px;top:697px;display:flex;gap:17px}
.slider-dots span{width:12px;height:12px;background:var(--white)}
.slider-dots span.off{background:none;border:1.5px solid var(--white)}
/* split sections */
.photo{position:absolute}
.frame{position:absolute;border:2px solid var(--blue)}
.section-title{position:absolute;font-family:'Montserrat',sans-serif;font-weight:700;font-size:41px;color:var(--ink)}
.copy{position:absolute;font-size:14.5px;line-height:36px;color:var(--text)}
.sub{position:absolute;font-family:'Montserrat',sans-serif;font-weight:600;font-size:18px;color:var(--blue)}
.checks{position:absolute;list-style:none;font-size:14.5px;color:var(--ink)}
.checks li{display:flex;align-items:center;height:36px;gap:24px}
.checks svg{width:13px;height:13px}
/* blog */
.blog-band{position:absolute;left:0;top:1956px;width:1200px;height:583px;background:linear-gradient(120deg,#d7e6f8 0%,#4d90ee 30%,#2f78e6 55%,#8cb8f0 75%,#3d84ea 100%)}
.blog-card{position:absolute;left:344px;top:2057px;width:512px;height:380px;background:rgba(28,108,242,.88);text-align:center;color:var(--white)}
.blog-card h2{margin-top:52px;font-family:'Montserrat',sans-serif;font-weight:700;font-size:41px}
.blog-card p{margin-top:22px;font-size:14.5px;line-height:31px;color:#dce8fd}
.blog-links{margin-top:17px;display:flex;justify-content:center;gap:48px;font-size:14.5px;color:#dce8fd;text-decoration:underline}
.btn-dark{display:inline-flex;margin-top:28px;width:195px;height:42px;background:#111;color:var(--white);font-size:15px;font-weight:500;align-items:center;justify-content:center}
/* products */
.products-title{position:absolute;left:0;top:2630px;width:1200px;text-align:center;font-family:'Montserrat',sans-serif;font-weight:700;font-size:41px;color:var(--ink)}
.product-card{position:absolute;top:2733px;width:297px;height:387px;background:var(--blue);border-radius:3px;text-align:center;color:var(--white)}
.product-card svg{margin-top:38px;width:64px;height:64px}
.product-card h3{margin-top:22px;font-weight:400;font-size:22px;letter-spacing:.5px}
.product-card p{margin:12px 30px 0;font-size:14px;line-height:25.5px;color:#dce8fd}
.product-card a{position:absolute;left:0;bottom:18px;width:100%;font-size:12.5px;font-weight:500;color:var(--white);text-decoration:underline}
/* footer */
.site-footer{position:absolute;left:0;top:3223px;width:1200px;height:226px;background:var(--footer);color:#e8e8e8;font-size:13.5px}
.contact-line{position:absolute;left:0;width:1200px;display:flex;justify-content:center;align-items:center;gap:14px}
.footer-social{position:absolute;left:0;top:3356px;width:1200px;display:flex;justify-content:center;gap:24px}
.footer-social .dot{width:15px;height:15px}
.copyright{position:absolute;left:0;top:3394px;width:1200px;text-align:center;font-size:13px;color:#e8e8e8}
</style>
</head>
<body>

<header class="site-header">
  <div class="brand"><span>Corventa Dx</span><span class="brand-square"></span></div>
  <span class="nav active" style="left:414px">HOME</span>
  <span class="nav" style="left:503px">ABOUT US</span>
  <span class="nav" style="left:624px">SERVICES</span>
  <span class="nav" style="left:742px">CONTACT US</span>
  <div class="social-block"><span class="dot"></span><span class="dot"></span><span class="dot"></span><span class="dot"></span></div>
</header>

<section class="hero" role="img" aria-label="Laboratory photo of a gloved hand with a pipette, DNA helix and healthcare keywords in blue tones"></section>
<div class="hero-kicker">Corventa Dx</div>
<div class="hero-title">Outside The Box Thinking</div>
<div class="btn-frame"></div>
<div class="btn-primary">LEARN MORE</div>
<div class="slider-dots"><span></span><span></span><span></span><span class="off"></span></div>

<!-- about -->
<div class="frame" style="left:74px;top:876px;width:551px;height:424px"></div>
<div class="photo" style="left:100px;top:848px;width:552px;height:425px;background:linear-gradient(135deg,#e6eef9,#b9cdea 55%,#d9e3f1)" role="img" aria-label="Laboratory bench with microscopes and a blue test tube rack"></div>
<h2 class="section-title" style="left:699px;top:870px">ABOUT US</h2>
<p class="copy" style="left:699px;top:938px;width:440px">Lorem ipsum dolor sit amet, consectetur adipiscing elit, sed do eiusmod tempor incididunt ut labore et dolore magna aliqua. Ut enim ad minim veniam, quis nostrud exercitation ullamco laboris nisi ut aliquip ex ea commodo consequat.</p>
<div class="sub" style="left:699px;top:1101px">Corventa Dx</div>
<ul class="checks" style="left:699px;top:1142px">
  <li><svg viewBox="0 0 14 14"><circle cx="7" cy="7" r="7" fill="#1c6cf2"/><path d="M3.8 7.2l2.2 2.1 4.2-4.4" stroke="#fff" stroke-width="1.7" fill="none"/></svg>Detection</li>
  <li><svg viewBox="0 0 14 14"><circle cx="7" cy="7" r="7" fill="#1c6cf2"/><path d="M3.8 7.2l2.2 2.1 4.2-4.4" stroke="#fff" stroke-width="1.7" fill="none"/></svg>Monitoring or</li>
  <li><svg viewBox="0 0 14 14"><circle cx="7" cy="7" r="7" fill="#1c6cf2"/><path d="M3.8 7.2l2.2 2.1 4.2-4.4" stroke="#fff" stroke-width="1.7" fill="none"/></svg>Management of diseases.</li>
</ul>

<!-- key challenges -->
<h2 class="section-title" style="left:74px;top:1440px">KEY CHALLENGES</h2>
<p class="copy" style="left:74px;top:1510px;width:470px;line-height:31px">Lorem ipsum dolor sit amet, consectetur adipiscing elit, sed do mod tempor incididunt ut labore et dolore magna aliqua. Ut enim ad minim veniam, quis nostrud exercitation ullamco laboris nisi ut aliquip ex ea commodo consequat.</p>
<div class="sub" style="left:74px;top:1651px">Medical Diagnostic</div>
<ul class="checks" style="left:74px;top:1691px">
  <li><svg viewBox="0 0 14 14"><circle cx="7" cy="7" r="7" fill="#1c6cf2"/><path d="M3.8 7.2l2.2 2.1 4.2-4.4" stroke="#fff" stroke-width="1.7" fill="none"/></svg>Designing</li>
  <li><svg viewBox="0 0 14 14"><circle cx="7" cy="7" r="7" fill="#1c6cf2"/><path d="M3.8 7.2l2.2 2.1 4.2-4.4" stroke="#fff" stroke-width="1.7" fill="none"/></svg>Evaluating</li>
  <li><svg viewBox="0 0 14 14"><circle cx="7" cy="7" r="7" fill="#1c6cf2"/><path d="M3.8 7.2l2.2 2.1 4.2-4.4" stroke="#fff" stroke-width="1.7" fill="none"/></svg>Marketing new products</li>
</ul>
<div class="frame" style="left:576px;top:1430px;width:550px;height:425px"></div>
<div class="photo" style="left:549px;top:1402px;width:550px;height:426px;background:linear-gradient(100deg,#c9ccd0,#eef0f1 35%,#9fa6ad 70%,#d8dcdf)" role="img" aria-label="Analytical laboratory instruments and computers in a lab"></div>

<!-- blog -->
<section class="blog-band" role="img" aria-label="Close-up photo of glass test tubes and pipette in blue light"></section>
<div class="blog-card">
  <h2>OUR LATEST BLOG</h2>
  <p>Lorem ipsum dolor sit amet, consectetur adipiscing elit, sed do<br>eiusmod tempor incididunt ut labore et dolore</p>
  <div class="blog-links"><span>View</span><span>Learn More</span></div>
  <span class="btn-dark">NEWS &amp; UPDATES</span>
</div>

<!-- products -->
<h2 class="products-title">MARKETING PRODUCTS</h2>
<div class="product-card" style="left:272px">
  <svg viewBox="0 0 64 64" fill="none" stroke="#fff" stroke-width="2"><rect x="6" y="6" width="52" height="38" rx="2"/><rect x="11" y="11" width="42" height="28"/><path d="M14 34l10-9 8 6 7-5 10 8"/><circle cx="42" cy="18" r="1.5"/><path d="M26 44v8M38 44v8M20 54h24"/></svg>
  <h3>DETECTION</h3>
  <p>Lorem ipsum dolor sit amet, consectetur adipiscing elit, sed do eiusmod tempor incididunt ut labore et dolore magna aliqua. Ut enim ad minim veniam, quis trud exercitation ullamco laboris nisi ut</p>
  <a>Learn More</a>
</div>
<div class="product-card" style="left:631px">
  <svg viewBox="0 0 64 64" fill="none" stroke="#fff" stroke-width="2"><rect x="6" y="6" width="52" height="38" rx="2"/><rect x="11" y="11" width="42" height="28"/><path d="M18 25c8-9 20-9 28 0-8 9-20 9-28 0z"/><circle cx="32" cy="25" r="4"/><path d="M26 44v8M38 44v8M20 54h24"/></svg>
  <h3>MONITORING</h3>
  <p style="margin-top:22px">Lorem ipsum dolor sit amet, consectetur adipiscing elit, sed do eiusmod tempor incididunt ut labore et dolore magna aliqua. Ut enim ad minim veniam, quis trud exercitation ullamco laboris nisi ut</p>
  <a>Learn More</a>
</div>

<!-- footer -->
<footer class="site-footer"></footer>
<div class="contact-line" style="top:3271px;color:#e8e8e8;font-size:13.5px">
  <svg width="14" height="11" viewBox="0 0 14 11"><rect width="14" height="11" rx="1" fill="#e8e8e8"/><path d="M1 1.5l6 4.5 6-4.5" stroke="#262528" stroke-width="1.3" fill="none"/></svg>
  <span style="text-decoration:underline">Email us at hello@corventadx.example</span>
</div>
<div class="contact-line" style="top:3306px;color:#e8e8e8;font-size:13.5px">
  <svg width="12" height="12" viewBox="0 0 24 24"><path fill="#e8e8e8" d="M6.6 10.8a15 15 0 006.6 6.6l2.2-2.2c.3-.3.7-.4 1-.2 1.1.4 2.3.6 3.6.6.6 0 1 .4 1 1V20c0 .6-.4 1-1 1A17 17 0 013 4c0-.6.4-1 1-1h3.5c.6 0 1 .4 1 1 0 1.3.2 2.5.6 3.6.1.3 0 .7-.2 1z"/></svg>
  <span>Call us at 555-014-2297</span>
</div>
<div class="footer-social"><span class="dot"></span><span class="dot"></span><span class="dot"></span><span class="dot"></span></div>
<div class="copyright">© 2019 Copyrights.The Company name. All Rights Reserved</div>

</body>
</html>
```